Verin Court Nine Flash website

we need a website to cater to 2 aspect of the business. We have Verin court residence and verin court office. For the office, we will get their inquire and arrange a face to face meetup to show them the office area for rent. For the residence side, it will need to be like lodgly or staymira.com. we want to allow them to book online for the date they need. We have a total of 10 different room configurations starting at $70 per night and up depending on the size of the room. example of the design is https://pelvandale.com/

Target Market(s)

the website should have detail information on the layout, designs, and luxury of the building.

Industry/Entity Type

office and service appartment rental/lease

Coding

Coded - Design and coding required

Number of Pages Required

5+ page

Requirements
Must have
• a luxury perspective
Nice to have
• example https://pelvandale.com/

```html
<!DOCTYPE html>
<html lang="en">
<head>
<meta charset="utf-8">
<title>Verin Court Nine</title>
<link href="https://fonts.googleapis.com/css2?family=Cinzel:wght@400;500;600&family=Poppins:wght@400;500;600&display=swap" rel="stylesheet">
<style>
:root{
  --gold:#d39c2c;
  --gold-light:#e2b559;
  --ink:#151515;
  --text:#2a2a2a;
  --muted:#7c7c7c;
  --line:#e4e4e4;
  --white:#ffffff;
  --mist:#ececec;
  --footer:#121212;
}
*{box-sizing:border-box;margin:0;padding:0}
html,body{width:1200px;height:4451px;overflow:hidden}
body{position:relative;font-family:'Poppins',sans-serif;color:var(--text);background:var(--white)}
.abs{position:absolute}
.serif{font-family:'Cinzel',serif}
.btn{position:absolute;display:flex;align-items:center;justify-content:center;background:var(--gold);color:var(--white);font-size:9px;font-weight:600;letter-spacing:.5px;text-transform:uppercase}
.photo{position:absolute}

/* header + hero */
.hero{position:absolute;left:0;top:0;width:1200px;height:583px;background:linear-gradient(100deg,#1b2130 0%,#2b3446 40%,#4a5568 62%,#262c38 100%)}
.nav{position:absolute;top:52px;left:112px;display:flex;gap:26px;font-size:9.5px;color:var(--white);text-transform:uppercase;letter-spacing:.3px}
.brand{position:absolute;top:70px;left:0;width:1200px;text-align:center;font-family:'Cinzel',serif;font-size:18px;color:var(--white);letter-spacing:.5px}
.search{position:absolute;top:42px;left:809px;width:188px;height:32px;border:1px solid rgba(255,255,255,.55);color:var(--white);font-size:10px;padding:8px 18px}
.search svg{position:absolute;right:10px;top:9px}
.login{top:42px;left:1013px;width:75px;height:32px;font-size:10px}
.hero-kicker{position:absolute;left:114px;top:222px;font-family:'Cinzel',serif;font-size:34px;color:var(--white);letter-spacing:1px}
.hero-title{position:absolute;left:113px;top:262px;font-family:'Cinzel',serif;font-size:54px;font-weight:500;color:var(--white);letter-spacing:1px}
.hero-copy{position:absolute;left:114px;top:332px;width:520px;font-size:15px;line-height:22px;color:var(--white)}

/* booking */
.booking{position:absolute;left:121px;top:519px;width:956px;height:143px;background:var(--white);box-shadow:0 4px 18px rgba(0,0,0,.08)}
.field{position:absolute;height:43px;border:1px solid var(--line);font-size:9.5px;color:#9a9a9a;padding:0 18px;display:flex;align-items:center;justify-content:space-between}
.tab{position:absolute;height:42px;display:flex;align-items:center;justify-content:center;font-size:9.5px;text-transform:uppercase}
.sketch-band{position:absolute;left:0;top:583px;width:1200px;height:140px;background:linear-gradient(180deg,#f7f7f7,#ffffff)}

/* about */
.about-copy h2{font-family:'Cinzel',serif;font-size:33px;font-weight:500;line-height:38px;color:var(--ink);letter-spacing:1px}
.sub{font-size:12.5px;color:var(--ink);text-transform:uppercase}
.para{font-size:12.5px;line-height:20px;color:#6d6d6d}

/* how it works */
.how{position:absolute;left:0;top:1273px;width:647px;height:485px;background:var(--ink)}
.how h2{position:absolute;left:116px;top:48px;font-family:'Cinzel',serif;font-size:33px;font-weight:500;color:var(--white);letter-spacing:1px}
.step{position:absolute;left:112px;display:flex;align-items:center;gap:14px;font-family:'Cinzel',serif;font-size:15px;color:var(--white);line-height:17px}
.num{flex:none;width:36px;height:36px;border-radius:50%;border:1.5px solid var(--white);display:flex;align-items:center;justify-content:center;font-size:17px}
.num.on{background:var(--gold);border-color:var(--gold)}
.overlay-title{font-family:'Cinzel',serif;font-size:20px;color:var(--white);letter-spacing:.5px}
.overlay-copy{font-size:12.5px;line-height:20px;color:var(--white)}

/* why choose */
.why h2{position:absolute;left:612px;top:1852px;font-family:'Cinzel',serif;font-size:33px;font-weight:500;color:var(--ink);letter-spacing:1px}
.card{position:absolute;width:221px;height:127px;border:1px solid var(--line);display:flex;flex-direction:column;align-items:center;justify-content:flex-end;padding-bottom:26px;gap:16px;font-family:'Cinzel',serif;font-size:12.5px;color:var(--ink)}
.card.active{background:var(--gold);border-color:var(--gold);color:var(--white)}
.watermark{position:absolute;left:-10px;top:2310px;width:1230px;text-align:center;font-family:'Cinzel',serif;font-size:136px;color:#f1f1f1;letter-spacing:6px;white-space:nowrap}

/* properties */
.section-title{position:absolute;left:0;width:1200px;text-align:center;font-family:'Cinzel',serif;font-size:33px;font-weight:500;color:var(--ink);letter-spacing:1px}
.prop{position:absolute;top:2516px;width:310px;height:342px;border:1px solid var(--line)}
.prop .photo{left:0;top:0;width:308px;height:211px}
.prop h3{position:absolute;left:18px;top:232px;font-family:'Cinzel',serif;font-size:14.5px;font-weight:500;color:var(--ink)}
.prop p{position:absolute;left:18px;top:258px;font-size:10px;line-height:17px;color:#888}
.prop a{position:absolute;left:18px;top:301px;font-size:10px;color:var(--gold);text-decoration:underline}

/* splash */
.splash{position:absolute;left:0;top:2974px;width:647px;height:486px;background:linear-gradient(90deg,#e6e6e6,#eeeeee)}
.splash h2{position:absolute;left:114px;top:128px;font-family:'Cinzel',serif;font-size:33px;font-weight:500;line-height:38px;color:var(--ink);letter-spacing:1px}

/* subscribe */
.subscribe{position:absolute;left:0;top:3908px;width:1200px;height:259px;background:var(--gold)}
.subscribe h2{position:absolute;left:0;top:116px;width:1200px;text-align:center;font-family:'Cinzel',serif;font-size:32px;font-weight:500;color:var(--white);letter-spacing:2px}
.sub-input{position:absolute;left:329px;top:171px;width:363px;height:43px;border:1px solid rgba(255,255,255,.7);color:var(--white);font-size:9.5px;padding:14px 16px}
.sub-btn{position:absolute;left:700px;top:171px;width:170px;height:43px;background:var(--white);color:var(--ink);font-size:9.5px;font-weight:600;display:flex;align-items:center;justify-content:center;text-transform:uppercase}

/* footer */
.footer{position:absolute;left:0;top:4167px;width:1200px;height:284px;background:var(--footer);color:var(--white)}
.contact-row{position:absolute;left:112px;display:flex;align-items:center;gap:8px;font-size:10.5px;font-weight:600;text-transform:uppercase}
.contact-row span.val{color:var(--gold);text-transform:none}
.foot-head{position:absolute;font-size:11px;font-weight:500;text-transform:uppercase;letter-spacing:.5px}
.links{position:absolute;left:804px;top:84px;font-size:10.5px;line-height:21.5px;list-style:none}
.foot-brand{position:absolute;left:0;top:156px;width:1200px;text-align:center;font-family:'Cinzel',serif;font-size:20px;color:var(--gold)}
.rule{position:absolute;left:0;top:224px;width:1200px;height:1px;background:#2c2c2c}
.copy{position:absolute;left:0;top:258px;width:1200px;text-align:center;font-size:10.5px}
</style>
</head>
<body>

<!-- Header & hero -->
<section class="hero" role="img" aria-label="Dusk photograph of a glass tower facade seen from below"></section>
<nav class="nav"><span>About us</span><span>Services</span><span>Reviews</span><span>Contact</span></nav>
<div class="abs" style="left:583px;top:22px;width:34px;height:34px;border:1.5px solid var(--white)"></div>
<div class="brand">Verin Court Nine</div>
<div class="search">Search
  <svg width="12" height="12" viewBox="0 0 12 12" fill="none" stroke="#fff" stroke-width="1.2"><circle cx="5" cy="5" r="3.8"/><line x1="8" y1="8" x2="11" y2="11"/></svg>
</div>
<div class="btn login">Log in</div>
<div class="hero-kicker">Welcome to</div>
<h1 class="hero-title">Verin Court Nine</h1>
<p class="hero-copy">Lorem ipsum dolor sit amet, consectetur adipiscing elit. Morbi semper mattis nunc, id viverra mi feugiat elementum.</p>

<div class="sketch-band" role="img" aria-label="Faint architectural line sketch of the building"></div>

<!-- Booking panel -->
<div class="booking">
  <div class="tab" style="left:16px;top:20px;width:184px;background:var(--gold);color:var(--white)">Overnight stays</div>
  <div class="tab" style="left:213px;top:20px;width:184px;border:1px solid var(--gold);color:var(--gold)">Day use stays</div>
  <div class="field" style="left:410px;top:20px;width:530px">Enter a destination or property</div>
  <div class="field" style="left:16px;top:76px;width:184px">Check In
    <svg width="14" height="12" viewBox="0 0 14 12" fill="none" stroke="#bbb"><rect x=".5" y="1.5" width="13" height="10"/><line x1=".5" y1="4.5" x2="13.5" y2="4.5"/><line x1="5" y1="4.5" x2="5" y2="11.5"/><line x1="9" y1="4.5" x2="9" y2="11.5"/><line x1=".5" y1="8" x2="13.5" y2="8"/></svg></div>
  <div class="field" style="left:213px;top:76px;width:184px">Check Out
    <svg width="14" height="12" viewBox="0 0 14 12" fill="none" stroke="#bbb"><rect x=".5" y="1.5" width="13" height="10"/><line x1=".5" y1="4.5" x2="13.5" y2="4.5"/><line x1="5" y1="4.5" x2="5" y2="11.5"/><line x1="9" y1="4.5" x2="9" y2="11.5"/><line x1=".5" y1="8" x2="13.5" y2="8"/></svg></div>
  <div class="field" style="left:410px;top:76px;width:147px">Location
    <svg width="10" height="14" viewBox="0 0 10 14" fill="none" stroke="#bbb"><path d="M5 13S1 8 1 5a4 4 0 0 1 8 0c0 3-4 8-4 8z"/><circle cx="5" cy="5" r="1.5"/></svg></div>
  <div class="field" style="left:568px;top:76px;width:124px">Adult
    <svg width="8" height="5" viewBox="0 0 8 5" fill="none" stroke="#bbb"><path d="M1 1l3 3 3-3"/></svg></div>
  <div class="field" style="left:703px;top:76px;width:124px">Child
    <svg width="8" height="5" viewBox="0 0 8 5" fill="none" stroke="#bbb"><path d="M1 1l3 3 3-3"/></svg></div>
  <div class="btn" style="left:833px;top:76px;width:107px;height:43px">Search</div>
</div>

<!-- About -->
<div class="photo" style="left:0;top:724px;width:553px;height:486px;background:linear-gradient(135deg,#9fb1c8 0%,#3d4350 45%,#23262d 70%,#8a96a8 100%)" role="img" aria-label="Modern dark residential tower with timber-framed windows against a pale sky"></div>
<div class="about-copy">
  <h2 class="abs" style="left:609px;top:828px">About Verin<br>Court Nine</h2>
  <div class="abs sub" style="left:609px;top:915px">Mauris semper lobortis lorem et sodales.</div>
  <p class="abs para" style="left:609px;top:943px;width:470px">Lorem ipsum dolor sit amet, consectetur adipiscing elit, sed do eiusmod tempor incididunt ut labore et dolore magna aliqua. Quis ipsum suspendisse ultrices gravida. Risus commodo viverra maecenas accumsan lacus vel facilisis.</p>
  <div class="btn" style="left:609px;top:1050px;width:133px;height:36px">Read more</div>
</div>

<!-- How it works -->
<section class="how">
  <h2>How it works</h2>
  <div class="step" style="top:115px"><span class="num on">1</span>Submit your service request</div>
  <div class="step" style="top:180px"><span class="num">2</span>We connect you with a certified service<br>technician</div>
  <div class="step" style="top:248px"><span class="num">3</span>A service technician will reach out to<br>you shortly</div>
  <div class="step" style="top:313px"><span class="num">4</span>Back to enjoying your backyard</div>
  <div class="btn" style="left:112px;top:387px;width:133px;height:36px">Request service</div>
</section>
<div class="photo" style="left:647px;top:1273px;width:553px;height:485px;background:linear-gradient(160deg,#c4ccd8 0%,#6f7c90 40%,#2d3543 75%,#1d222c 100%)" role="img" aria-label="Glass skyscrapers photographed from street level looking up"></div>
<div class="abs step" style="left:674px;top:1561px;gap:10px"><span class="num">1</span><span class="overlay-title">Submit your service request</span></div>
<p class="abs overlay-copy" style="left:721px;top:1601px;width:380px">Donec nec semper nisl. Suspendisse lacus tellus, dictum eu pretium et, interdum ut nibh. Suspendisse viverra mauris sed maximus ultricies. Class aptent taciti sociosqu ad litora torquent per conubia nostra, per inceptos himenaeos.</p>

<!-- Why choose us -->
<div class="photo" style="left:0;top:1821px;width:553px;height:486px;background:linear-gradient(200deg,#d9dee5 0%,#8693a5 35%,#3a4454 70%,#232a35 100%)" role="img" aria-label="Converging glass office towers seen from below"></div>
<div class="abs overlay-title" style="left:150px;top:2112px;width:303px;text-align:right">Worry free guarantee</div>
<svg class="abs" style="left:466px;top:2101px" width="46" height="48" viewBox="0 0 46 48" fill="none" stroke="#fff" stroke-width="1.6"><circle cx="23" cy="20" r="14"/><circle cx="23" cy="20" r="10"/><path d="M18 20l4 4 7-8"/><path d="M14 31l-5 13 7-3 4 6 3-10M32 31l5 13-7-3-4 6-3-10"/></svg>
<p class="abs overlay-copy" style="left:100px;top:2149px;width:353px;text-align:right">Lorem ipsum dolor sit amet, consectetur adipiscing elit. Nulla consequat tortor a quam maximus laoreet. Nam dapibus sem malesuada arcu euismod, et posuere eros ullamcorper. Sed euismod neque in ligula aliquam sollicitudin.</p>

<section class="why">
  <h2>Why choose us</h2>
  <div class="card active" style="left:610px;top:1917px">
    <svg width="46" height="50" viewBox="0 0 46 50" fill="none" stroke="#fff" stroke-width="1.6"><circle cx="23" cy="20" r="15"/><circle cx="23" cy="20" r="10"/><path d="M18 20l4 4 7-8"/><path d="M14 32l-5 14 7-3 4 6 3-10M32 32l5 14-7-3-4 6-3-10"/></svg>
    Worry free guarantee</div>
  <div class="card" style="left:849px;top:1917px">
    <svg width="60" height="44" viewBox="0 0 60 44" fill="none" stroke="var(--gold)" stroke-width="1.6" stroke-linejoin="round"><path d="M2 14l10-8 10 6 8-4 10 2 8-6 10 8"/><path d="M12 6l-8 20 6 6M48 4l8 20-8 8"/><path d="M22 12l-6 8 4 3 8-6 14 12-4 4-6-5M40 32l-4 4-6-5M32 37l-3 3-5-4"/></svg>
    No contracts, ever</div>
  <div class="card" style="left:610px;top:2063px">
    <svg width="48" height="48" viewBox="0 0 48 48" fill="none" stroke="var(--gold)" stroke-width="1.8"><circle cx="24" cy="24" r="21"/><path d="M24 11v14h9"/></svg>
    Show up on time</div>
  <div class="card" style="left:849px;top:2063px">
    <svg width="60" height="60" viewBox="0 0 60 60" fill="none" stroke="var(--gold)" stroke-width="1.6"><path d="M14 4v34"/><path d="M8 38h12l2 18H6z"/><path d="M32 26h22l-3 30H35z"/><path d="M36 26v-6h14v6"/><path d="M43 20V10"/><circle cx="30" cy="10" r="2"/><circle cx="24" cy="18" r="1.5"/></svg>
    Total clean promise</div>
  <div class="btn" style="left:609px;top:2222px;width:134px;height:34px">Learn more</div>
</section>

<!-- Properties -->
<div class="watermark">Verin Court Nine</div>
<h2 class="section-title" style="top:2440px">Our properties</h2>

<article class="prop" style="left:112px">
  <div class="photo" style="background:linear-gradient(180deg,#5c82b6 0%,#9eb6d3 45%,#3e5368 100%)" role="img" aria-label="Curved glass towers against a blue sky with clouds"></div>
  <h3>Bramwell Close, Fernley, CH4</h3>
  <p>3 Bedroom Semi-Detached House<br>in Fernley</p>
  <a>Explore now</a>
</article>
<article class="prop" style="left:446px">
  <div class="photo" style="background:linear-gradient(180deg,#2b6fb8 0%,#5f95cc 45%,#254a72 100%)" role="img" aria-label="Cluster of blue glass high-rise offices"></div>
  <h3>Ashcombe Street, Pellow, CH2</h3>
  <p>4 Bedroom Terraced House<br>in Pellow</p>
  <a>Explore now</a>
</article>
<article class="prop" style="left:778px">
  <div class="photo" style="background:linear-gradient(180deg,#4e7fb3 0%,#7fb2a4 50%,#2e5a56 100%)" role="img" aria-label="Green-tinted glass building with angular facade"></div>
  <h3>Harlow Road, Dunmere, CH2</h3>
  <p>3 Bedroom Semi-Detached House<br>in Dunmere</p>
  <a>Explore now</a>
</article>
<div class="btn" style="left:541px;top:2891px;width:118px;height:31px">Explore more</div>

<!-- Splash -->
<section class="splash" role="presentation">
  <h2>We make a splash with<br>our customers</h2>
  <div class="abs" style="left:114px;top:219px;font-size:12.5px;color:var(--ink)">Mara Linden</div>
  <p class="abs para" style="left:114px;top:248px;width:480px;font-size:11.5px">Never hesitate when it comes to potential electrical problems. Electrical issues can quickly develop into major catastrophes.</p>
  <div class="btn" style="left:114px;top:313px;width:107px;height:35px">View all</div>
</section>
<div class="photo" style="left:647px;top:2974px;width:553px;height:486px;background:linear-gradient(135deg,#1f4f86 0%,#6d9cc7 40%,#c7d9ea 60%,#35679a 100%)" role="img" aria-label="Close view of a blue reflective glass curtain wall"></div>

<!-- Completed projects -->
<h2 class="section-title" style="top:3510px">Completed projects</h2>
<div class="photo" style="left:0;top:3584px;width:114px;height:211px;background:linear-gradient(180deg,#aab7c6,#4c5a6b)" role="img" aria-label="Office tower facade"></div>
<div class="photo" style="left:133px;top:3584px;width:298px;height:211px;background:linear-gradient(180deg,#8fb3d6 0%,#6c8aa3 50%,#3f5a52 100%)" role="img" aria-label="City skyline with high-rises and harbour"></div>
<div class="photo" style="left:451px;top:3584px;width:299px;height:211px;background:linear-gradient(160deg,#0f2f7a 0%,#2e63c4 50%,#a8c5ea 100%)" role="img" aria-label="Deep blue glass towers seen from below"></div>
<div class="photo" style="left:769px;top:3584px;width:300px;height:211px;background:linear-gradient(180deg,#b8c5d4 0%,#6d7989 55%,#3b4450 100%)" role="img" aria-label="Downtown high-rise buildings under an overcast sky"></div>
<div class="photo" style="left:1086px;top:3584px;width:114px;height:211px;background:linear-gradient(180deg,#5e86b6,#c5d3e3)" role="img" aria-label="Skyscraper corner against the sky"></div>
<div class="btn" style="left:541px;top:3825px;width:118px;height:31px">Explore more</div>

<!-- Subscribe -->
<section class="subscribe">
  <div class="abs" style="left:583px;top:36px;width:34px;height:34px;border:1.5px solid var(--white)"></div>
  <h2>Subscribe for latest updates</h2>
  <div class="sub-input">Enter Email</div>
  <div class="sub-btn">Subscribe</div>
</section>

<!-- Footer -->
<footer class="footer">
  <div class="contact-row" style="top:68px">
    <svg width="18" height="12" viewBox="0 0 18 12" fill="var(--gold)"><rect width="18" height="12"/><path d="M0 0l9 7 9-7" stroke="#121212" stroke-width="1.2" fill="none"/></svg>
    Email address: <span class="val">support@verincourtnine.com</span></div>
  <div class="contact-row" style="top:106px">
    <svg width="16" height="16" viewBox="0 0 16 16" fill="none" stroke="var(--gold)" stroke-width="1.6"><path d="M3 1l3 3-2 2c1 2 3 4 5 5l2-2 3 3-2 3C7 14 2 9 1 3z"/></svg>
    Call &amp; discuss your pool needs: <span class="val">(877) 555-0148</span></div>
  <div class="contact-row" style="top:155px;font-size:9.5px">Follow us:
    <span style="width:10px;height:10px;border-radius:50%;background:var(--gold);display:inline-block;margin-left:4px"></span>
    <span style="width:10px;height:10px;border-radius:50%;background:var(--gold);display:inline-block"></span>
    <span style="width:10px;height:10px;border-radius:50%;background:var(--gold);display:inline-block"></span>
  </div>

  <div class="abs" style="left:583px;top:78px;width:34px;height:34px;border:1.5px solid var(--gold)"></div>
  <div class="foot-brand">Verin Court Nine</div>

  <div class="foot-head" style="left:804px;top:60px">Usefull links</div>
  <ul class="links"><li>About Us</li><li>Services</li><li>Reviews</li><li>Pricing</li><li>Contact</li></ul>

  <div class="foot-head" style="left:975px;top:60px">Our location</div>
  <div class="abs" style="left:975px;top:86px;width:113px;height:89px;background:linear-gradient(135deg,#cfe0c8,#e6eadf 50%,#bdd3e0)" role="img" aria-label="Small street map showing the building location"></div>

  <div class="rule"></div>
  <div class="copy">Copyright © 2024. All rights reserved.</div>
</footer>

</body>
</html>
```